The Larkmoor Lodge 5 Bedroom Cayman Islands Guest House offering weekly rentals

I am in need of a website for my 5 bedroom guest house in the Cayman Islands.
I have operated this guest house for almost three years. As the sites I am currently located on have raised their charges over the past year; I have decided to host my own site.
The site should reflect island retreat type style. With Tropical, ocean colors
Here are the core requirements I can think of.
• A comprehensive vacation rental web site
• Multiple languages if possible
• Pictures & video – of property, what’s close & the island
• Property description
• Reservation/Booking calendar.
• Information on where to go
• Social media links, such as a PalBoard & Snapgrove
• Shared moments - Event, celebration and guest photos
• Reviews page
• Rates
• Email interaction/Messaging
• Credit card processing… (Be able to securely hold the credit card information to manually process using a credit card machine (Within 24 hours)
I have already started a site on HostNook but got lost so once agreed I would hand over the codes as they would also be hosting the site.

Info on the house:

This spacious vacation home is a 5 minute walk away from Driftwood Cove Shore and has a supermarket across the street. A small shopping plaza with a bank, pharmacy and 24 hour Munchline is a one minute walk away. No car? No problem! The public bus stops right in front of the house, runs along Long Pearl Strand and on to George Town. Take a 5 minute bus ride to Luzon Quay; an outdoor mall with restaurants, shops, Reelhaus and home to the islands only observation tower.

The home boasts a fully loaded kitchen with granite counter tops, six burner gas stove, large capacity refrigerator and two dishwashers perfect for feeding a large family or group.
State of the art media room with a 73 inch high definition television, GX4, complete surround sound and plush recliners providing hours of entertainment.
Downstairs, the master suite has a comfortable memory foam king bed and an en-suite bathroom with a granite double vanity and whirlpool tub. Perfect for relaxing after a long day at the beach. Downstairs also has a cozy Queen bedroom and a serene King bedroom that shares a full bathroom. There’s an additional half-bath for added convenience.
The upstairs is a spacious double Queen bedroom and a double Full bedroom that shares a bathroom. In total the house sleeps up to 14 people very comfortably.
The screened in back porch can be accessed from the media room, downstairs Master bedroom and Queen bedroom. It’s the ideal escape to enjoy the fresh Cayman breeze without the insects.
To spare you the hassle of laundry; we’ve even provided two washers and two dryers! Leaving you more time for the beach.
For the vacation Mom, no need to worry, we have a full size crib, Tot-A-Nook Play pen, 2 full size high chairs and a car seat!

Target Market(s)

Families or groups seeking to vacation in the Caribbean or the tropics.

Industry/Entity Type

Hotel

Contact Information for Business Card

Business card front
The Larkmoor Lodge
Guest House
Your Cayman home away from home!
1786 Coral Hollow Rd, Grand Cayman, Cayman Islands
Tel: (345) 555-0187
Email: thelarkmoorlodge@palmnest.com

Business card back
Pictures of house
5 bedroom home walking distance to the beach!
Air-conditioned, Wi-Fi, cable TV, sleeps up to 14
Book online www.thelarkmoorlodge.net
Like us on PalBoard

Number of Pages Required

5+ page

Font styles to use
Script

Requirements
Must have
• Multiple languages if possible (English, Spanish, French)
• • Pictures & video – of property, what’s close & the island
• • Property description
• • Reservation/Booking calendar.
• • Information on where to go
• • Social media links, such as a PalBoard & Snapgrove
• • Shared moments - Event, celebration and guest photos
• • Reviews page
• • Rates
• • Email interaction/Messaging
• • Credit card processing… (Be able to securely hold the credit card information to manually process using a credit card machine (Within 24 hours)
Nice to have
• Slide show of the house on the home page
Should not have
• Too many dark colors

```html
<!DOCTYPE html>
<html lang="en">
<head>
<meta charset="utf-8">
<title>The Larkmoor Lodge – Cayman Guest House</title>
<link rel="stylesheet" href="https://fonts.googleapis.com/css2?family=Playfair+Display:wght@400;700&family=Open+Sans:wght@400;600&display=swap">
<style>
:root{
  --teal:#1ba3c6;
  --teal-dark:#0f7e9e;
  --orange:#f7a51c;
  --navy:#0d2c4a;
  --ocean:#1d5f8c;
  --sky:#3aa0d8;
  --aqua:#22b3b7;
  --grey-bg:#eef2f4;
  --nav-bg:#f4f4f4;
  --text:#4a5a66;
  --white:#ffffff;
}
*{margin:0;padding:0;box-sizing:border-box}
html,body{width:880px;height:1200px;overflow:hidden}
body{font-family:"Open Sans",Arial,sans-serif;color:var(--text);background:var(--white);font-size:11px}
.serif{font-family:"Playfair Display",Georgia,serif}

.site-header{height:45px;display:flex;align-items:center;justify-content:space-between;padding:0 70px}
.brand{font-family:"Playfair Display",Georgia,serif;color:var(--teal);font-size:17px;font-weight:700;letter-spacing:.5px}
.tagline{font-size:9px;color:#8a969e}
.header-tools{display:flex;gap:6px;align-items:center}
.lang-chip{width:14px;height:10px;background:#c9d3da}
.social-chip{width:12px;height:12px;background:var(--teal)}
.social-chip.alt{background:var(--orange)}

.main-nav{height:35px;background:var(--nav-bg);display:flex;padding:0 70px;border-top:1px solid #e5e5e5;border-bottom:1px solid #e5e5e5}
.main-nav a{display:flex;align-items:center;padding:0 13px;font-size:10px;color:#56636b;text-decoration:none}
.main-nav a.active{background:var(--orange);color:var(--white)}

.hero{position:relative;height:240px}
.hero-photo{position:absolute;inset:0;background:linear-gradient(180deg,#8ebfd9 0%,#c9b27a 45%,#6a8a4e 75%,#8a8a7a 100%)}
.hero-content{position:absolute;inset:0;display:flex;flex-direction:column;align-items:center;color:var(--white);padding-top:40px}
.hero-title{font-family:"Playfair Display",Georgia,serif;font-size:36px}
.hero-sub{font-size:12px;text-align:center;margin-top:8px;line-height:1.4}
.hero-actions{position:absolute;bottom:38px;left:0;right:0;display:flex;justify-content:center;gap:40px;align-items:center}
.btn{display:inline-block;background:var(--orange);color:var(--white);border-radius:14px;padding:6px 22px;font-size:10px;font-weight:600}
.btn.sky{background:var(--sky)}
.hero-link{color:var(--white);font-size:10px}
.hero-arrow{position:absolute;top:100px;width:24px;height:24px}

.welcome{background:var(--grey-bg);padding:14px 70px 18px;height:280px}
.welcome-card{background:var(--white);height:100%;padding:18px 26px}
.welcome-top{display:flex;justify-content:space-between}
.welcome-text{width:420px}
.section-title{font-family:"Playfair Display",Georgia,serif;color:var(--teal);font-size:22px}
.welcome-text p{margin-top:10px;line-height:1.5;font-size:10px}
.check-dates{width:180px;border-left:1px solid #e1e7ea;padding-left:20px}
.check-dates .section-title{font-size:20px;line-height:1.15}
.check-dates .btn{margin-top:10px}
.stats{display:flex;gap:8px;margin-top:22px}
.stat{flex:1;border:1px solid #e1e7ea;height:72px;text-align:center;padding-top:8px}
.stat.highlight{background:#e9f6fa;border-color:var(--teal)}
.stat b{display:block;font-family:"Playfair Display",Georgia,serif;color:var(--teal);font-size:24px;font-weight:400}
.stat span{font-size:8px;line-height:1.2;display:block;padding:0 4px}
.center{text-align:center;margin-top:18px}

.gallery{height:235px;text-align:center;padding-top:22px}
.gallery .section-title{font-size:24px}
.strip{display:flex;margin-top:14px;height:110px}
.shot{flex:1}
.shot.video{position:relative}
.shot.video svg{position:absolute;left:50%;top:50%;transform:translate(-50%,-50%)}
.gallery .btn{margin-top:18px}

.island{position:relative;height:205px;color:var(--white);text-align:center}
.island-photo{position:absolute;inset:0;background:linear-gradient(160deg,#134a73 0%,#1d6c98 45%,#2a8fb5 70%,#164d78 100%)}
.island-content{position:relative;padding-top:34px}
.island-title{font-family:"Playfair Display",Georgia,serif;font-size:32px}
.island-title small{font-size:16px;margin-right:4px}
.island-content p{width:500px;margin:16px auto 0;font-size:10px;line-height:1.6}

.cta-row{display:flex;height:90px}
.cta{flex:1;display:flex;align-items:center;padding:0 70px;color:var(--white)}
.cta.where{background:var(--sky)}
.cta.contact{background:var(--aqua);justify-content:flex-end}
.cta h3{font-family:"Playfair Display",Georgia,serif;font-size:24px;font-weight:400}
.cta p{font-size:9px;margin-top:4px}

.site-footer{height:70px;background:var(--navy);display:flex;align-items:center;justify-content:space-between;padding:0 70px;color:#9fb4c6;font-size:9px}
.site-footer nav{display:flex;gap:22px}
.footer-icons{display:flex;gap:6px}
.footer-icons span{width:12px;height:12px;background:#4d6a86}
</style>
</head>
<body>

<header class="site-header">
  <div class="brand">THE LARKMOOR LODGE</div>
  <div class="tagline">Your Cayman home away from home</div>
  <div class="header-tools">
    <span class="lang-chip" aria-label="English"></span>
    <span class="lang-chip" aria-label="Español"></span>
    <span class="social-chip" aria-label="PalBoard"></span>
    <span class="social-chip alt" aria-label="Snapgrove"></span>
  </div>
</header>

<nav class="main-nav">
  <a class="active">Home</a><a>Property</a><a>Amenities</a><a>Rates</a><a>Where to go</a><a>Shared moments</a><a>Reviews</a><a>Gallery</a><a>Contact</a>
</nav>

<section class="hero">
  <div class="hero-photo" role="img" aria-label="Photo of the guest house facade with palm trees and blue sky"></div>
  <div class="hero-content">
    <h1 class="hero-title">Rent our residence</h1>
    <p class="hero-sub">5 bedroom guest house, sleeps 14<br>steps from the beach</p>
  </div>
  <div class="hero-actions">
    <span class="btn sky">Reserve now</span>
    <span class="hero-link">View gallery</span>
  </div>
  <svg class="hero-arrow" style="left:50px" viewBox="0 0 24 24"><path d="M15 5l-7 7 7 7" fill="none" stroke="#fff" stroke-width="2.5"/></svg>
  <svg class="hero-arrow" style="right:50px" viewBox="0 0 24 24"><path d="M9 5l7 7-7 7" fill="none" stroke="#fff" stroke-width="2.5"/></svg>
</section>

<section class="welcome">
  <div class="welcome-card">
    <div class="welcome-top">
      <div class="welcome-text">
        <h2 class="section-title">Welcome to our site residence</h2>
        <p>This spacious vacation home is a 5 minute walk away from Driftwood Cove Shore and has a supermarket across the street.</p>
        <p>A small shopping plaza with a bank, pharmacy and a food place is a one minute walk away.</p>
      </div>
      <div class="check-dates">
        <h2 class="section-title">Check dates<br>and make reservation</h2>
        <span class="btn">Book now</span>
      </div>
    </div>
    <div class="stats">
      <div class="stat"><b>14</b><span>Sleeps people in comfort</span></div>
      <div class="stat highlight"><b>5</b><span>Bedrooms</span></div>
      <div class="stat"><b>5</b><span>Minute walk to public beach</span></div>
      <div class="stat"><b>2</b><span>Bathrooms</span></div>
      <div class="stat"><b>1</b><span>Half bath downstairs</span></div>
      <div class="stat"><b>1</b><span>Minute walk to the plaza</span></div>
    </div>
    <div class="center"><span class="btn">Read more</span></div>
  </div>
</section>

<section class="gallery">
  <h2 class="section-title">Pictures &amp; videos our residence</h2>
  <div class="strip">
    <div class="shot" role="img" aria-label="Pool and loungers by the sea" style="background:linear-gradient(#4a90c8,#2b6fa0)"></div>
    <div class="shot" role="img" aria-label="Turquoise beach with resort" style="background:linear-gradient(#5fb7d8,#2d86b8)"></div>
    <div class="shot" role="img" aria-label="House exterior with garden" style="background:linear-gradient(#a89a6a,#6e7a48)"></div>
    <div class="shot" role="img" aria-label="Bedroom interior" style="background:linear-gradient(#c99a66,#8a5a34)"></div>
    <div class="shot video" role="img" aria-label="Video of the beach at sunset" style="background:linear-gradient(#7a8a9a,#3e4e60)">
      <svg width="36" height="36" viewBox="0 0 36 36"><path d="M12 8l16 10-16 10z" fill="#fff"/></svg>
    </div>
  </div>
  <span class="btn">View all gallery</span>
</section>

<section class="island">
  <div class="island-photo" role="img" aria-label="Aerial view of the Cayman Islands coastline and ocean"></div>
  <div class="island-content">
    <h2 class="island-title"><small>The</small>Cayman Islands</h2>
    <p>Clear turquoise water, soft white sand and a relaxed island pace. Take the bus along Long Pearl Strand to George Town, or visit Luzon Quay for shops, dining, the Reelhaus cinema and the island's only observation tower.</p>
  </div>
</section>

<section class="cta-row">
  <div class="cta where"><div><h3>Where to go</h3><p>Beaches, dining and island sights</p></div></div>
  <div class="cta contact"><div><h3>Contact with us</h3><p>thelarkmoorlodge@palmnest.com</p></div></div>
</section>

<footer class="site-footer">
  <nav><span>Home</span><span>Property</span><span>Amenities</span><span>Rates</span><span>Where to go</span><span>Reviews</span><span>Contact</span></nav>
  <div class="footer-icons"><span aria-label="PalBoard"></span><span aria-label="Snapgrove"></span></div>
</footer>

</body>
</html>
```